Seeking funky, innovative business cards

I am looking to refresh our current business cards to something more engaging, visual and impactful. We are a management consultancy firm, see website (www.thornbury-partners.com.au). I've included our colour scheme, sample of the slides we use and our old business cards. We would like our cards to have icons. The card should display:- Name- Title- Mobile number- Address- Email address- Website - Company logo- Our purpose statement "We help teams build workplaces worth joining"

Contact Information for Business Card

Radek Solvieri
Consultant
0491 627 358
Level 3, 218 Wexford Street, Melbourne 3000
radek@thornbury-partners.com.au
www.thornbury-partners.com.au

Purpose statement "We help teams build workplaces worth joining"
LOGO available in google images

Font styles to use
Other font styles liked:
• Open Sans Light, Bebas Neue (open to other cool foints)

Colors
ffc214
5c5c5c
f5f5f5
fefefe

Requirements
Must have
• - Name
• - Title
• - Mobile number
• - Address
• - Email address
• - Website
• - Company logo
• - Our purpose statement "We help teams build workplaces worth joining"
Nice to have
• - Icons
• - Colour (see our colour scheme"

```html
<!DOCTYPE html>
<html lang="en">
<head>
<meta charset="utf-8">
<title>Thornbury Partners — Business Card</title>
<link href="https://fonts.googleapis.com/css2?family=Bebas+Neue&family=Open+Sans:wght@300;400;700&display=swap" rel="stylesheet">
<style>
  :root {
    --brand-yellow: #ffc214;
    --brand-grey: #5c5c5c;
    --paper-light: #f5f5f5;
    --paper-white: #fefefe;
    --ink-dark: #4a4a4a;
  }
  * { margin: 0; padding: 0; box-sizing: border-box; }
  html, body {
    width: 1200px;
    height: 800px;
    overflow: hidden;
  }
  body {
    background: var(--paper-light);
    font-family: "Open Sans", sans-serif;
    position: relative;
  }
  .card {
    position: absolute;
    top: 260px;
    width: 490px;
    height: 280px;
    border-radius: 4px;
    box-shadow: 0 10px 28px rgba(0, 0, 0, 0.14), 0 2px 6px rgba(0, 0, 0, 0.08);
    overflow: hidden;
  }
  .card--contact {
    left: 80px;
    background: var(--brand-yellow);
    color: var(--ink-dark);
    padding: 34px 40px;
  }
  .card--brand {
    left: 630px;
    background: var(--paper-white);
    display: flex;
    align-items: center;
    justify-content: center;
  }
  .holder-name {
    font-weight: 700;
    font-size: 22px;
    line-height: 1.1;
    color: var(--brand-grey);
  }
  .holder-title {
    font-weight: 400;
    font-size: 14px;
    margin-top: 2px;
    color: var(--ink-dark);
  }
  .contact-list {
    list-style: none;
    margin-top: 20px;
  }
  .contact-item {
    display: flex;
    align-items: flex-start;
    gap: 12px;
    font-size: 12.5px;
    line-height: 1.35;
    margin-bottom: 5px;
    color: var(--ink-dark);
  }
  .contact-icon {
    width: 15px;
    height: 15px;
    flex: 0 0 15px;
    margin-top: 1px;
    fill: var(--paper-white);
  }
  .purpose-statement {
    position: absolute;
    right: 28px;
    bottom: 18px;
    font-family: "Bebas Neue", sans-serif;
    font-size: 15px;
    letter-spacing: 0.06em;
    white-space: nowrap;
    color: var(--paper-white);
  }
  .brand-lockup {
    display: flex;
    align-items: center;
    gap: 12px;
  }
  .brand-dot {
    width: 12px;
    height: 12px;
    border-radius: 50%;
    background: var(--brand-yellow);
  }
  .brand-name {
    font-family: "Open Sans", sans-serif;
    font-weight: 300;
    font-size: 34px;
    color: var(--brand-grey);
    letter-spacing: 0.01em;
  }
</style>
</head>
<body>

  <section class="card card--contact" aria-label="Contact side of business card">
    <h1 class="holder-name">Radek Solvieri</h1>
    <p class="holder-title">Consultant</p>

    <ul class="contact-list">
      <li class="contact-item">
        <svg class="contact-icon" viewBox="0 0 16 16" aria-hidden="true">
          <path d="M8 0.5a5 5 0 0 0-5 5c0 3.8 5 10 5 10s5-6.2 5-10a5 5 0 0 0-5-5zm0 7a2 2 0 1 1 0-4 2 2 0 0 1 0 4z"/>
        </svg>
        <span>Level 3, 218 Wexford Street<br>Melbourne 3000</span>
      </li>
      <li class="contact-item">
        <svg class="contact-icon" viewBox="0 0 16 16" aria-hidden="true">
          <path d="M3.6 1.2l2.2 2.6c.3.4.3.9 0 1.3L4.7 6.3a9.5 9.5 0 0 0 5 5l1.2-1.1c.4-.3.9-.3 1.3 0l2.6 2.2c.4.3.4.9.1 1.3l-1 1.1c-.5.5-1.2.7-1.9.5C6.6 13.9 2.1 9.4.7 4c-.2-.7 0-1.4.5-1.9l1.1-1c.4-.3 1-.3 1.3.1z"/>
        </svg>
        <span>0491 627 358</span>
      </li>
      <li class="contact-item">
        <svg class="contact-icon" viewBox="0 0 16 16" aria-hidden="true">
          <path d="M1 3h14v10H1zM2.3 4.2v.3L8 8.6l5.7-4.1v-.3zM2.3 6v5.8h11.4V6L8 10.1z"/>
        </svg>
        <span>radek@thornbury-partners.com.au</span>
      </li>
      <li class="contact-item">
        <svg class="contact-icon" viewBox="0 0 16 16" aria-hidden="true">
          <path d="M8 1a7 7 0 1 0 0 14A7 7 0 0 0 8 1zm5.4 6.3h-2.3a11 11 0 0 0-1-4.1 5.6 5.6 0 0 1 3.3 4.1zM8 2.5c.7.9 1.5 2.6 1.7 4.8H6.3C6.5 5.1 7.3 3.4 8 2.5zM5.9 3.2a11 11 0 0 0-1 4.1H2.6a5.6 5.6 0 0 1 3.3-4.1zM2.6 8.7h2.3a11 11 0 0 0 1 4.1 5.6 5.6 0 0 1-3.3-4.1zM8 13.5c-.7-.9-1.5-2.6-1.7-4.8h3.4c-.2 2.2-1 3.9-1.7 4.8zm2.1-.7a11 11 0 0 0 1-4.1h2.3a5.6 5.6 0 0 1-3.3 4.1z"/>
        </svg>
        <span>www.thornbury-partners.com.au</span>
      </li>
    </ul>

    <p class="purpose-statement">We help teams build workplaces worth joining</p>
  </section>

  <section class="card card--brand" aria-label="Brand side of business card">
    <div class="brand-lockup">
      <span class="brand-dot" aria-hidden="true"></span>
      <span class="brand-name">Thornbury Partners</span>
    </div>
  </section>

</body>
</html>
```